Local massage therapist needs some new marketing material

Hi there! I am a massage therapist here in Denver, CO in Brindle Hollow(shopping and art district) of the city. My business is called Lunora Massage of Denver. My practice has an eastern influence and I do reflexology, thai massage and use Chinese herbs, etc. I know all my clients and pay close attention to details. I am also very respectful of tradition and it shows in how I work. I tend to like modern, clean, fun, Asian designs. I am wanting a new business card and brochure. I have a logo and branding for my business that I want used in the design. Currently, the sign for my building is purple and I think my logo was designed to be purple. I will attach pictures of it and can send whatever files are necessary so it can be integrated into the brochure, etc. I like the purple but open to using other colors as well. Thanks!
My website is lunoramassagestudio.example where info can be gathered about me and services/fees for brochure.
Updates

Just increased budget. Please see new feedback in discussion thread.

Thanks!

                                       HEY ALL,

Just wanted to let you know that I made a change to my website. It is on the Prices Page. I no longer have the frequent  flyer prices but I added discounts. Let me know if you have any questions. Thanks so much!

Target Market(s)

healthy, urban, educated, upper middle class, yogis

Industry/Entity Type

Marketing

Requirements
Must have
• logo stays purple
Should not have
• not too busy

```html
<!DOCTYPE html>
<html lang="en">
<head>
<meta charset="utf-8">
<title>Lunora Massage of Denver – Brochure</title>
<link href="https://fonts.googleapis.com/css2?family=Source+Sans+3:wght@300;400;600;700&family=Josefin+Sans:wght@300&display=swap" rel="stylesheet">
<style>
  :root {
    --backdrop: #cfdcda;
    --paper: #f7f7f8;
    --paper-shade: #e9e9ec;
    --ink: #2b2b2b;
    --muted: #8a8a8a;
    --charcoal: #2d3033;
    --lavender: #dcb4ee;
    --violet: #5a2fe0;
    --lime: #79e01c;
    --stone-dark: #3e3e3e;
    --stone-light: #9a9a9a;
    --orchid: #b06be6;
    --skin: #c9a08a;
  }
  * { box-sizing: border-box; margin: 0; padding: 0; }
  html, body { width: 1200px; height: 900px; overflow: hidden; }
  body {
    background: var(--backdrop);
    font-family: "Source Sans 3", Arial, sans-serif;
    color: var(--ink);
    position: relative;
  }
  .brochure {
    position: absolute; left: 100px; top: 80px;
    width: 1000px; height: 740px;
    background: var(--paper);
    box-shadow: 0 2px 6px rgba(0,0,0,.25);
    overflow: hidden;
  }
  .panel {
    position: absolute; top: 0; bottom: 0; width: 333.33px;
    background: linear-gradient(90deg, var(--paper) 0%, #fbfbfc 60%, var(--paper-shade) 100%);
  }
  .panel--left { left: 0; }
  .panel--middle { left: 333.33px; }
  .panel--right { left: 666.66px; background: linear-gradient(90deg, var(--paper-shade) 0%, #fbfbfc 25%, var(--paper) 100%); }

  .hero {
    position: absolute; left: 0; right: 0; top: 16px; height: 222px;
    background:
      radial-gradient(ellipse 22% 45% at 36% 50%, var(--orchid) 0%, #8f4fcf 55%, transparent 72%),
      radial-gradient(ellipse 20% 40% at 10% 60%, var(--stone-light), transparent 70%),
      radial-gradient(ellipse 18% 35% at 62% 75%, var(--stone-light), transparent 70%),
      linear-gradient(180deg, #6a6a6a, var(--stone-dark));
  }
  .hero-bar {
    position: absolute; left: 0; right: 0; top: 238px; height: 22px;
    background: var(--charcoal);
  }
  .brand {
    position: absolute; left: 760px; top: 48px; width: 150px;
    text-align: center; color: #ffffff;
    font-family: "Josefin Sans", "Source Sans 3", sans-serif;
    font-weight: 300; font-size: 24px; letter-spacing: 4px; line-height: 1;
  }
  .brand-dot {
    display: block; margin: 0 auto 18px;
    width: 78px; height: 78px; border-radius: 50%;
    border: 1.5px solid #ffffff;
  }

  .intro {
    position: absolute; left: 60px; top: 282px; width: 252px;
    font-size: 10px; line-height: 12.6px; text-align: justify;
  }
  .benefits {
    position: absolute; left: 68px; top: 460px; width: 250px;
    list-style: none; font-size: 10px; line-height: 12px;
  }
  .benefits li { height: 18.6px; }

  .photo { position: absolute; background: linear-gradient(135deg, #e8d7c8, var(--skin)); }
  .photo--cupping { left: 372px; top: 280px; width: 250px; height: 100px; background: linear-gradient(90deg, #7a9a5a, #e6d2c0 40%, #f0e6dc); }
  .photo--towel   { left: 372px; top: 392px; width: 122px; height: 82px; background: linear-gradient(135deg, #b07a5a, #f3ede0); }
  .photo--herbal  { left: 372px; top: 484px; width: 122px; height: 96px; background: linear-gradient(135deg, #a8782a, #d8b07a 50%, #f2e8d8); }
  .photo--stones  { left: 372px; top: 590px; width: 122px; height: 90px; background: linear-gradient(135deg, #f0eeea, var(--skin) 60%, #8a5e46); }
  .photo--thai    { left: 504px; top: 382px; width: 122px; height: 298px; background: linear-gradient(180deg, #6e6e6e, #3a3a3a 60%, #f2f2f2); }

  .services { position: absolute; left: 700px; top: 262px; width: 260px; }
  .services h2 {
    color: var(--violet); font-weight: 400; font-size: 32px; line-height: 40px; margin-bottom: 42px;
  }
  .service { color: var(--lime); font-weight: 700; font-size: 12.5px; line-height: 16px; height: 28px; }
  .service--last { height: auto; margin-bottom: 3px; }
  .extras { list-style: none; color: var(--muted); font-size: 9.5px; line-height: 12px; }
  .extras li { height: 16.5px; }

  .footer-band {
    position: absolute; left: 0; right: 0; top: 690px; height: 32px;
    background: var(--lavender);
  }
</style>
</head>
<body>
  <main class="brochure">
    <section class="panel panel--left"></section>
    <section class="panel panel--middle"></section>
    <section class="panel panel--right"></section>

    <div class="hero" role="img" aria-label="Purple orchid resting on grey river stones"></div>
    <div class="hero-bar"></div>
    <div class="brand"><span class="brand-dot"></span>LUNORA</div>

    <p class="intro">These days, in addition to "rubbing," massage therapy, often referred to as bodywork or somatic therapy, refers to the application of various techniques to the muscular structure and soft tissues of the body that include applying fixed or movable pressure, holding, vibration, rocking, friction, kneading and compression using primarily the hands, although massage therapists do use other areas of the body, such as the forearms, elbows or feet. All of the techniques are used for the benefit of the musculoskeletal, circulatory-lymphatic, nervous, and other systems of the body. In fact, massage therapy positively influences the overall health and well-being of the client. It's physical and mental benefits include:</p>
    <ul class="benefits">
      <li>Relaxing the whole body</li>
      <li>Loosening and relieving tired, aching and tight muscles</li>
      <li>Increasing flexibility and range of motion</li>
      <li>Diminishing chronic pain</li>
      <li>Calming the nervous system</li>
      <li>Lowering blood pressure and heart rate</li>
      <li>Enhancing skin tone</li>
      <li>Aiding in recovery following injuries and illness</li>
      <li>Strengthening the immune system</li>
      <li>Reducing headaches and mental stress</li>
      <li>Improving relaxation</li>
      <li>Promoting restful sleep</li>
    </ul>

    <div class="photo photo--cupping" role="img" aria-label="Client relaxing during a fire cupping treatment"></div>
    <div class="photo photo--towel" role="img" aria-label="Client draped in a towel on a massage table"></div>
    <div class="photo photo--herbal" role="img" aria-label="Client resting during a Thai herbal compress session"></div>
    <div class="photo photo--stones" role="img" aria-label="Hot stones placed along a client's back"></div>
    <div class="photo photo--thai" role="img" aria-label="Therapist guiding a client through a Thai massage stretch"></div>

    <section class="services">
      <h2>Services</h2>
      <p class="service">Colorado Rain (Seasonal Treatment)</p>
      <p class="service">Offered only at 90 mins - $75</p>
      <p class="service">Swedish Escape</p>
      <p class="service">Deep Tissue Therapy</p>
      <p class="service">Table Thai Massage</p>
      <p class="service">Blend Massage</p>
      <p class="service">Prenatal Bliss</p>
      <p class="service service--last">Extra Massage Treats</p>
      <ul class="extras">
        <li>Chinese Fire Cupping</li>
        <li>Hot Stones</li>
        <li>Reflexology</li>
        <li>Thai Herbal Compress</li>
      </ul>
    </section>

    <div class="footer-band"></div>
  </main>
</body>
</html>
```